Website for online Real Estate School

I need to have three drop boxes which are really the main item on our web site. These tabs will need to be front and center “call to action”. Our sole goal on our site is to sell real estate courses which will be connected to these drop boxes. So please make this “call to action” section “clean” and the main emphasis on the page. We will fill in the items in the drop box so please ensure we have that ability.

 Get your license
 Post-Licensing
 Continuing Education

You could use the statement; “The Path to Your Future”

I’d like the design to be one where you keep scrolling down instead of having 5 or 6 tabs up top with different pages.

As you scan down I’d like to include the graphics and text as shown on one of the attachments. I copied this from another site so I’d ask you provide another logo. I already amended the text

People enter the real estate field with diverse educational backgrounds and overall goals. Some enter to only work part time to supplement their current income, and others full time. One person may enter the commercial market space and another residential. There is a wide range of directions you can take and the sky is truly the limit. Whichever path you take, your chances of success are directly related to your level of preparation and commitment. This is one career that really rewards self-motivated individuals.

 Careers - Career fields include residential and commercial real estate agents, brokers, mortgage brokers, property managers and independent investors. Many of these careers are held by independent people who have a strong entrepreneurial spirit. As you enter the real estate business in general its not unlikely you will be in it for life in one way or another. In our opinion it truly is the best path to wealth.
 Salary - According to the U.S. Office of Workforce Tallies, real estate brokers earned a median annual wage of $56,860 and the highest 10 percent earned more than $166,940. An agent’s income is only limited to how much work you want to put into your business. We highly suggest you consider a few of our partners offers below as they can truly help you work smarter, not harder.
 Degrees - A real estate license will provide all you will need to enter the real estate business. Each state has requirements that you complete “Continuing Education” every other year. There are several other courses that will provide you with certifications which demonstrate your sophistication therefore we recommend you continue your pursuit of education and we certainly hope you do so with us.

We highly recommend you consider a few of out strategic partners as their services are a tremendous advantage to real estate professionals.

Here we will have 6-8 banners from companies that we will be affiliates with.

At this point I’m not interested in providing an address nor phone number for contact.

Our web site domain is; www.HarborlineLearning.com

I have a number of graphics that I will upload the .ai file. Feel free to improve as you see fit.

I included a few copies of our competition. PLEASE, do some basic research.... in short, we are a national school that sells real estate licensing education for your initial license and also continuing education. We sooooooo want to be better than our competitors. Please help us achieve this. google real estate license and real estate continuing education and look at competitors... Please. That way you truly know what we need to beat.

This is my 40th ish project on pixel forum and appreciate everyone's work which is why I always come back.

We will be EXTREMELY RESPONSIVE AND LOG ON 5-10X A DAY TO COMMENT ON DESIGNS. PLEASE ONLY MESSAGE US ON THE DESIGN ITSELF VS VIA THE MAIL SYSTEM AS ITS EASIER FOR US. THANKS!!!

Reason: We have extended this project for 5 days as we think 2 days was a bit ambitious. We look forward to your designs

Target Market(s)

18-40 year old consumers. Aspiring and existing real estate agents and brokers

Industry/Entity Type

Real Estate

Coding

Coded - Design and coding required

Number of Pages Required

1 page

Font styles to use
Other font styles liked:
• your choice

Requirements
Must have
• clean site... please review the competition by searching on google; real estate continuing education and real estate license
Nice to have
• just clean site. nice and simple and be sure to have the call to action sections as the emphasis

```html
<!DOCTYPE html>
<html lang="en">
<head>
<meta charset="utf-8">
<title>Harborline Learning</title>
<link href="https://fonts.googleapis.com/css2?family=Open+Sans:wght@400;600;700&display=swap" rel="stylesheet">
<style>
:root{
  --orange:#ff7a00;
  --orange-dark:#f26b00;
  --ink:#333333;
  --text:#777777;
  --light:#f3f3f3;
  --footer-top:#555555;
  --footer-bottom:#3a3a3a;
  --white:#ffffff;
}
*{margin:0;padding:0;box-sizing:border-box}
html,body{width:718px;height:1200px;overflow:hidden;background:var(--white)}
body{font-family:"Open Sans",Arial,sans-serif;color:var(--ink);position:relative}
.abs{position:absolute}

/* header */
.site-header{position:absolute;left:0;top:0;width:718px;height:54px;border-top:2px solid var(--orange);background:var(--white);border-bottom:1px solid #e6e6e6}
.brand{position:absolute;left:95px;top:13px;display:flex;align-items:center;gap:6px}
.brand-mark{width:12px;height:12px;background:var(--orange);border-radius:50%}
.brand-name{font-weight:700;font-size:10px;color:#4a4a4a;letter-spacing:.2px}
.main-nav{position:absolute;top:24px;left:0;font-size:7px;font-weight:600;color:#444;text-transform:uppercase}
.main-nav span{position:absolute;white-space:nowrap}
.main-nav .active{color:var(--orange)}
.nav-pointer{position:absolute;left:304px;top:49px;width:0;height:0;border-left:4px solid transparent;border-right:4px solid transparent;border-bottom:4px solid var(--orange)}

/* hero */
.hero{position:absolute;left:0;top:54px;width:718px;height:276px;background:var(--light);overflow:hidden}
.hero-photo{position:absolute;left:254px;top:0;width:464px;height:276px;background:linear-gradient(90deg,#f3f3f3 0%,#e9e4e1 30%,#c9a996 55%,#3a2a26 80%,#8a1f26 100%)}
.hero-title{position:absolute;left:96px;top:88px;font-size:22px;font-weight:600;color:var(--ink)}
.hero-title em{font-style:normal;color:var(--orange)}
.hero-copy{position:absolute;left:96px;top:125px;width:260px;font-size:8.5px;line-height:15px;color:var(--text)}
.btn{position:absolute;background:var(--orange);color:var(--white);font-weight:700;font-size:7px;text-align:center;text-transform:uppercase}
.hero-btn{left:96px;top:161px;width:115px;height:22px;line-height:22px;border-bottom:2px solid var(--orange-dark)}
.slider-arrow{position:absolute;top:128px;width:20px;height:20px;border:1px solid #bbb;border-radius:50%;background:rgba(255,255,255,.3)}

/* welcome */
.house-art{position:absolute;left:112px;top:345px;width:184px;height:200px;background:linear-gradient(180deg,#e8e8e8 0%,#d9d9d9 60%,#bcd8a6 100%);border-radius:4px}
.welcome-title{position:absolute;left:331px;top:372px;font-size:14.5px;font-weight:600;color:var(--ink)}
.welcome-title em{font-style:normal;color:var(--orange)}
.welcome-lead{position:absolute;left:332px;top:399px;width:270px;font-size:8.5px;line-height:13px;color:var(--orange)}
.welcome-body{position:absolute;left:332px;top:437px;width:289px;font-size:6.4px;line-height:11.7px;color:var(--text);text-align:justify}

/* offer */
.offer{position:absolute;left:0;top:547px;width:718px;height:229px;background:var(--orange);color:var(--white)}
.offer-title{position:absolute;top:23px;width:100%;left:4px;text-align:center;font-size:14px;font-weight:600}
.offer-item{position:absolute;top:65px;width:180px;text-align:center}
.offer-icon{margin:0 auto;width:58px;height:58px;border:3px solid var(--white);border-radius:50%;display:flex;align-items:center;justify-content:center}
.offer-icon-inner{width:46px;height:46px;border-radius:50%;background:var(--white);display:flex;align-items:center;justify-content:center}
.offer-name{margin-top:13px;font-size:9.5px;font-weight:600}
.offer-text{margin:8px auto 0;width:140px;font-size:6.6px;line-height:11.3px}
.offer-more{margin-top:6px;font-size:6.6px}
.offer-arrow{position:absolute;top:85px}

/* services */
.services-title{position:absolute;top:795px;width:100%;text-align:center;font-size:14px;font-weight:600;color:var(--ink)}
.services-title em{font-style:normal;color:var(--orange)}
.service{position:absolute;top:832px;width:165px}
.service-photo{height:92px;border:2px solid #e3e3e3;box-shadow:0 0 2px #ccc}
.service-name{margin-top:9px;font-size:8.5px;color:var(--orange)}
.service-text{margin-top:5px;font-size:6.5px;line-height:11.7px;color:var(--text)}
.service-more{margin-top:8px;font-size:6.3px;font-weight:600;color:var(--ink)}

/* footer */
.site-footer{position:absolute;left:0;top:1024px;width:718px;height:137px;background:linear-gradient(180deg,var(--footer-top),var(--footer-bottom));color:var(--white)}
.footer-col{position:absolute;top:31px;font-size:6.8px;line-height:13.6px}
.footer-col h3{font-size:9px;font-weight:600;margin-bottom:3px;text-transform:uppercase}
.newsletter-input{width:144px;height:19px;background:var(--white);border-radius:2px;color:#888;padding-left:7px;line-height:19px;margin-top:6px}
.newsletter-btn{position:static;display:block;width:70px;height:22px;line-height:22px;margin-top:7px;font-size:7.5px}
.bottom-bar{position:absolute;left:0;top:1161px;width:718px;height:39px;background:var(--orange);color:var(--white)}
.copyright{position:absolute;left:97px;top:15px;font-size:6.3px}
.social{position:absolute;top:11px;width:17px;height:17px;border:1px solid var(--white);border-radius:50%}
</style>
</head>
<body>

<header class="site-header">
  <div class="brand"><span class="brand-mark"></span><span class="brand-name">HARBORLINE LEARNING</span></div>
  <nav class="main-nav">
    <span class="active" style="left:299px">Home</span>
    <span style="left:350px">About</span>
    <span style="left:403px">Careers</span>
    <span style="left:464px">Salary</span>
    <span style="left:519px">Degeree</span>
    <span style="left:579px">Contact Us</span>
  </nav>
  <span class="nav-pointer"></span>
</header>

<section class="hero">
  <div class="hero-photo" role="img" aria-label="Smiling graduate in cap and gown holding a diploma"></div>
  <h1 class="hero-title"><em>To Path To Your</em> Future</h1>
  <p class="hero-copy">Lorem ipsum dolor sit amet, consectetur adipiscing elit, sed do eiusmod tempor incididunt ut laborelorem ipmo.</p>
  <div class="btn hero-btn">More Info</div>
  <span class="slider-arrow" style="left:17px"><svg width="18" height="18" viewBox="0 0 18 18"><path d="M10 6l-3 3 3 3" fill="none" stroke="#999" stroke-width="1"/></svg></span>
  <span class="slider-arrow" style="left:682px"><svg width="18" height="18" viewBox="0 0 18 18"><path d="M8 6l3 3-3 3" fill="none" stroke="#999" stroke-width="1"/></svg></span>
</section>

<section class="welcome">
  <div class="house-art" role="img" aria-label="Illustration of a small white house with shrubs"></div>
  <h2 class="welcome-title"><em>WELCOME TO</em> HARBORLINE LEARNING</h2>
  <p class="welcome-lead">Lorem ipsum dolor sit amet, consectetur adipiscing elit, sed deiu sm tempor incididunt ut laborelorem ipmo.</p>
  <p class="welcome-body">Sed ut perspiciatis unde omnis iste natus error sit voluptatem accusantium dolore mq ue laudantium, totam rem aperiam, eaque ipsa quae ab illo inventore veritatis et quasi archit ecto beatae vitae dicta sunt explicabo. Nemo enim ipsam volupta tem quia volup tas sit aspernatur aut odit aut fugit, sed quia conse quun tur mag ni dolores eos qui rati one voluptatem sequi nesciunt atur aut odit aut fugit, sed quia conse quun tur mag ni dolores eos qui rati one voluptatem sequi nesciunt.</p>
</section>

<section class="offer">
  <h2 class="offer-title">WHAT WE OFFER</h2>

  <div class="offer-item" style="left:91px">
    <div class="offer-icon"><div class="offer-icon-inner">
      <svg width="22" height="22" viewBox="0 0 22 22"><rect x="5" y="3" width="12" height="15" rx="1" fill="none" stroke="#ff7a00" stroke-width="2"/><path d="M8 8h6M8 12h6" stroke="#ff7a00" stroke-width="1.6"/></svg>
    </div></div>
    <div class="offer-name">Get your license</div>
    <p class="offer-text">Sed ut perspiciatis unde otsrs itvoluptatem accusan tium dolore mq ue laudpta te iu dololorlo</p>
    <div class="offer-more">Read More &gt;&gt;</div>
  </div>

  <div class="offer-item" style="left:270px">
    <div class="offer-icon"><div class="offer-icon-inner">
      <svg width="22" height="22" viewBox="0 0 22 22"><rect x="3" y="7" width="16" height="11" rx="1.5" fill="#ff7a00"/><rect x="8" y="4" width="6" height="4" rx="1" fill="none" stroke="#ff7a00" stroke-width="1.6"/></svg>
    </div></div>
    <div class="offer-name">Post-Licensing</div>
    <p class="offer-text">Sed ut perspiciatis unde otsrs itvoluptatem accusan tium dolore mq ue laudpta te iu dololorlo</p>
    <div class="offer-more">Read More &gt;&gt;</div>
  </div>

  <div class="offer-item" style="left:458px">
    <div class="offer-icon"><div class="offer-icon-inner">
      <svg width="22" height="22" viewBox="0 0 22 22"><path d="M7 3h11l-3 15H4z" fill="none" stroke="#ff7a00" stroke-width="1.8" stroke-linejoin="round"/><path d="M8 8h6M7.5 11h6" stroke="#ff7a00" stroke-width="1.4"/></svg>
    </div></div>
    <div class="offer-name">Continuing Education</div>
    <p class="offer-text">Sed ut perspiciatis unde otsrs itvoluptatem accusan tium dolore mq ue laudpta te iu dololorlo</p>
    <div class="offer-more">Read More &gt;&gt;</div>
  </div>

  <svg class="offer-arrow" style="left:243px" width="56" height="24" viewBox="0 0 56 24"><path d="M2 18 Q24 0 48 16" fill="none" stroke="#ffa04d" stroke-width="4"/><path d="M42 8l9 11-13 0z" fill="#ffa04d"/></svg>
  <svg class="offer-arrow" style="left:430px" width="56" height="24" viewBox="0 0 56 24"><path d="M2 18 Q24 0 48 16" fill="none" stroke="#ffa04d" stroke-width="4"/><path d="M42 8l9 11-13 0z" fill="#ffa04d"/></svg>
</section>

<h2 class="services-title"><em>OUR</em> SERVICES</h2>

<article class="service" style="left:95px">
  <div class="service-photo" role="img" aria-label="Person climbing a long staircase toward light" style="background:linear-gradient(180deg,#e9ebea,#9fa3a2 60%,#2e3534)"></div>
  <div class="service-name">Careers</div>
  <p class="service-text">Sed ut p loerspiciatis unde omnis iste natus error sit volup tatem accusantium dolore mq uloe laud antium, tota m rem aperiam, eaque ipsa quae ab.</p>
  <div class="service-more">READ MORE &raquo;</div>
</article>
<article class="service" style="left:276px">
  <div class="service-photo" role="img" aria-label="Businessman with crossed arms among falling money" style="background:linear-gradient(180deg,#e4e6e6,#b9bcbd 55%,#7d7f80)"></div>
  <div class="service-name">Salary</div>
  <p class="service-text">Sed ut p loerspiciatis unde omnis iste natus error sit volup tatem accusantium dolore mq uloe laud antium, tota m rem aperiam, eaque ipsa quae ab.</p>
  <div class="service-more">READ MORE &raquo;</div>
</article>
<article class="service" style="left:457px">
  <div class="service-photo" role="img" aria-label="Happy graduate with raised arms behind a stack of books" style="background:linear-gradient(180deg,#f1f0e2,#e2dcc4 55%,#c8b99a)"></div>
  <div class="service-name">Degrees</div>
  <p class="service-text">Sed ut p loerspiciatis unde omnis iste natus error sit volup tatem accusantium dolore mq uloe laud antium, tota m rem aperiam, eaque ipsa quae ab.</p>
  <div class="service-more">READ MORE &raquo;</div>
</article>

<footer class="site-footer">
  <div class="footer-col" style="left:96px">
    <h3>Contact Us</h3>
    <div>Phone : 55501234</div>
    <div style="margin-top:1px">Email &nbsp;: hello@harborlinelearning.com</div>
    <div style="margin-top:1px">48 Quay Lane</div>
    <div style="margin-top:1px">Oregon USA.</div>
  </div>
  <div class="footer-col" style="left:256px">
    <h3>Resources</h3>
    <div>Home</div><div>About</div><div>Careers</div><div>Salary</div><div>Degrees</div>
  </div>
  <div class="footer-col" style="left:366px">
    <h3>Support</h3>
    <div>Get Lisence</div><div>Privacy Policy</div><div>Contact</div>
  </div>
  <div class="footer-col" style="left:476px">
    <h3>Sign Up Newsletter</h3>
    <div>Please sign up here for latest deals</div>
    <div class="newsletter-input">Email address</div>
    <div class="btn newsletter-btn">SUBSCRIBE</div>
  </div>
</footer>

<div class="bottom-bar">
  <p class="copyright">&copy; 2016 harborline learning. All rughts reserved &nbsp;Term of Use</p>
  <span class="social" style="left:525px"></span>
  <span class="social" style="left:545px"></span>
  <span class="social" style="left:565px"></span>
  <span class="social" style="left:585px"></span>
  <span class="social" style="left:605px"></span>
</div>

</body>
</html>
```